Talvane Companies Business Card Design

We need a new business card for our Private Equity Real Estate Development firm, “Talvane” and our EB-5 regional center “Moorfield Regional Center” on one card. We prefer a design that is simple, elegant, and represents the luxury products we design and build as well as the financial security and stability our successful history has produced. We are an industry leader in our field and 3rd generation family business that has evolved into an institutional quality investment platform. Considered design size is standard business card dimensions (3.5 x 2 inches with an additional 1/8 inch space for design elements or backgrounds that extend beyond the finished size of your piece.

Target Market(s)

• High net worth individuals
• Highly skilled technical workers and physicians in the US seeking investment-based immigration opportunities
• Sophisticated private equity investors
• Intermediary partners include domestic attorneys and investment brokers, as well as international agent networks
• US real estate developers

Industry/Entity Type

Finance

Contact Information for Business Card

(Providing placeholder info for personal information, please design for longer character spaces, longer names and addresses etc..)
• Logo for Talvane
• Logo for Moorfield Regional Center
• Full name: Dorian Talvane
• Job title: CEO
• Email address: dtalvane@talvanecompanies.example
• Cell phone number: +1.555.318.4476
• Office number +1.555.240.6185
• Office address: Quillan Court 5, 4817 Vista Ardell, Larkmoor, NV.
• Website: www.talvanecompanies.example

Font styles to use
Serif
Sans Serif

Colors
ec1f27
ffffff
000000

Requirements
Must have
• • Logo for Talvane
• • Logo for Moorfield Regional Center
• - Use rounded corners
• (See .ai file included for logos)
Nice to have
• • Simple, elegant design
• • Aesthetically compatible with our website design (www.talvanecompanies.example)
• • Color palette including but not limited to white, black, and red (as per logos)
Should not have
• - Not too much red color
• - Do not stack both logos on top of each other

```html
<!DOCTYPE html>
<html lang="en">
<head>
<meta charset="utf-8">
<title>Moorfield Regional Center – Business Card</title>
<link rel="stylesheet" href="https://fonts.googleapis.com/css2?family=Lato:wght@400;700&display=swap">
<style>
  :root {
    --canvas: #e9e9ea;
    --card-white: #ffffff;
    --card-red: #8e1a2c;
    --card-red-dark: #731526;
    --brand-red: #e01b2a;
    --mark-red: #9a1a30;
    --ink: #333333;
    --ink-soft: #555555;
    --on-red: #ece6e7;
  }
  * { box-sizing: border-box; margin: 0; padding: 0; }
  html, body { width: 1200px; height: 900px; overflow: hidden; }
  body {
    background: var(--canvas);
    font-family: "Lato", Arial, sans-serif;
    color: var(--ink);
    position: relative;
  }
  .card {
    position: absolute;
    left: 250px;
    width: 700px;
    height: 400px;
    border-radius: 22px;
    overflow: hidden;
    box-shadow: 0 10px 28px rgba(0,0,0,.18);
  }
  .card--front { top: 40px; background: var(--card-white); }
  .card--back {
    top: 470px;
    background: linear-gradient(135deg, var(--card-red), var(--card-red-dark));
    display: flex; align-items: center; justify-content: center;
    padding: 0 48px;
  }

  .brand { display: flex; align-items: center; gap: 14px; }
  .brand__square { width: 34px; height: 34px; background: var(--mark-red); border-radius: 4px; flex: none; }
  .brand__name {
    font-family: "Lato", Arial, sans-serif;
    font-weight: 700;
    color: var(--mark-red);
    font-size: 19px;
    letter-spacing: 1.5px;
    text-transform: uppercase;
    line-height: 1.1;
    white-space: nowrap;
  }
  .card--front .brand { position: absolute; left: 48px; top: 42px; }

  .card--back .brand { gap: 20px; }
  .card--back .brand__square { width: 50px; height: 50px; background: var(--on-red); opacity: .9; }
  .card--back .brand__name { color: var(--on-red); font-size: 28px; letter-spacing: 2.5px; }

  .person { position: absolute; left: 48px; top: 112px; }
  .person__name {
    color: var(--brand-red);
    font-weight: 700;
    font-size: 34px;
    letter-spacing: .5px;
    text-transform: uppercase;
    line-height: 1;
  }
  .person__title { font-size: 17px; color: var(--ink-soft); margin-top: 6px; }

  .address {
    position: absolute; left: 48px; top: 196px;
    font-size: 16px; line-height: 1.35; color: var(--ink);
    width: 300px;
  }

  .contact { position: absolute; left: 48px; top: 252px; list-style: none; }
  .contact li {
    display: flex; align-items: center; gap: 10px;
    font-size: 16px; line-height: 26px; color: var(--ink);
  }
  .contact svg { width: 13px; height: 13px; flex: none; }
  .contact .accent { color: var(--brand-red); }

  .decor-block {
    position: absolute; right: 56px; top: 96px;
    width: 230px; height: 230px;
    border-radius: 18px;
    background: linear-gradient(145deg, #a11d33, #6e1226);
  }
</style>
</head>
<body>

<section class="card card--front" aria-label="Business card front">
  <div class="brand">
    <span class="brand__square" aria-hidden="true"></span>
    <span class="brand__name">Moorfield Regional Center</span>
  </div>

  <div class="person">
    <h1 class="person__name">Dorian Talvane</h1>
    <p class="person__title">CEO</p>
  </div>

  <p class="address">Quillan Court 5, 4817 Vista Ardell,<br>Larkmoor, NV.</p>

  <ul class="contact">
    <li>
      <svg viewBox="0 0 16 16" aria-hidden="true"><path fill="#e01b2a" d="M4 1l3 3-2 2c1 2 3 4 5 5l2-2 3 3-2 2C7 14 2 9 2 3z"/></svg>
      +1.555.318.4476
    </li>
    <li>
      <svg viewBox="0 0 16 16" aria-hidden="true"><rect x="4" y="1" width="8" height="14" rx="2" fill="#e01b2a"/><rect x="6" y="3" width="4" height="8" fill="#fff"/></svg>
      +1.555.240.6185
    </li>
    <li>
      <svg viewBox="0 0 16 16" aria-hidden="true"><rect x="1" y="3" width="14" height="10" rx="1" fill="none" stroke="#e01b2a" stroke-width="1.6"/><path d="M1.5 4l6.5 5 6.5-5" fill="none" stroke="#e01b2a" stroke-width="1.6"/></svg>
      dtalvane@talvanecompanies.example
    </li>
    <li>
      <svg viewBox="0 0 16 16" aria-hidden="true"><circle cx="8" cy="8" r="6.5" fill="none" stroke="#e01b2a" stroke-width="1.6"/><path d="M1.5 8h13M8 1.5c-3 3-3 10 0 13M8 1.5c3 3 3 10 0 13" fill="none" stroke="#e01b2a" stroke-width="1.2"/></svg>
      <span>www.<span class="accent">talvanecompanies.example</span></span>
    </li>
  </ul>

  <div class="decor-block" role="img" aria-label="Large brand emblem area"></div>
</section>

<section class="card card--back" aria-label="Business card back">
  <div class="brand">
    <span class="brand__square" aria-hidden="true"></span>
    <span class="brand__name">Moorfield Regional Center</span>
  </div>
</section>

</body>
</html>
```